Kelvo Car Audio - Stationary Needed
Business Card, Letterhead, Envelope, Fax Cover, E-mail Signature
Kelvo Car Audio - Stationary Needed -
Creative Brief
Use specific fonts
Designers discretion
Professional
Marcus Feltin
President / CEO
4182 W. Linden Ave. Santa Ana, CA 92817
marc@kelvocaraudio.example
www.kelvocaraudio.example
For business card, use Black background w/ White font.
Would like map of our location, along with the following services we offer: - Car Audio Sales and Installation - Remote Start / Vehicle Security - GPS Navigation - Phone & Wireless Integration - Custom and Pre-Fab Enclosures - Professional Window Tint

```html
<!DOCTYPE html>
<html lang="en">
<head>
<meta charset="utf-8">
<title>Kelvo Car Audio – Stationery Set</title>
<link href="https://fonts.googleapis.com/css2?family=Montserrat:wght@700&family=Open+Sans:wght@400;600&display=swap" rel="stylesheet">
<style>
  :root{
    --stage:#e6e6e4;
    --paper:#ffffff;
    --ink:#1a1a1a;
    --muted:#6b6b6b;
    --faint:#ececec;
    --accent:#2b8fd8;
    --card-dark:#111111;
    --map-base:#d9d4c4;
    --map-road:#f2eee2;
  }
  *{box-sizing:border-box;margin:0;padding:0}
  html,body{width:1200px;height:924px;overflow:hidden}
  body{background:var(--stage);font-family:"Open Sans",Arial,sans-serif;color:var(--ink);position:relative}
  .brand-name{font-family:"Montserrat",Arial,sans-serif;font-weight:700;color:var(--ink);letter-spacing:.02em;white-space:nowrap}
  .sheet{position:absolute;background:var(--paper);box-shadow:0 2px 8px rgba(0,0,0,.18);overflow:hidden}

  /* Letterhead */
  .letterhead{left:60px;top:150px;width:440px;height:570px;padding:36px 40px}
  .letterhead .brand-name{font-size:22px}
  .letterhead .tagline{font-size:7px;color:var(--accent);letter-spacing:.18em;text-transform:uppercase;margin-top:3px}
  .letter{margin-top:34px;font-size:7.5px;line-height:1.7;color:#444}
  .letter p{margin-bottom:9px}
  .letter .recipient{margin-bottom:14px}
  .letter .signoff{margin-top:18px}
  .letter .signoff strong{display:block;margin-top:22px;color:var(--ink);font-weight:600}
  .watermark{position:absolute;right:28px;bottom:46px;font-family:"Montserrat",Arial,sans-serif;font-weight:700;font-size:58px;color:var(--faint)}
  .letter-footer{position:absolute;left:40px;right:40px;bottom:22px;border-top:1px solid var(--ink);padding-top:6px;font-size:6px;color:var(--muted);display:flex;justify-content:space-between}

  /* Business cards */
  .card{width:250px;height:143px;padding:16px 18px}
  .card-front .brand-name{font-size:17px}
  .card-front .holder{position:absolute;top:16px;right:18px;text-align:right}
  .card-front .holder b{display:block;font-size:9px;font-weight:600}
  .card-front .holder span{font-size:6.5px;color:var(--accent)}
  .card-front .contact{position:absolute;left:18px;bottom:14px;font-size:6.5px;line-height:1.6;color:var(--muted)}
  .card-back{background:var(--card-dark);color:#fff;display:flex;gap:10px;padding:16px 14px 16px 16px}
  .card-back .services{flex:1;font-size:6px;line-height:1.7;white-space:nowrap}
  .card-back h4{font-size:7px;color:var(--accent);font-weight:600;margin-bottom:4px;text-transform:uppercase;letter-spacing:.08em}
  .card-back h4.find{margin-top:5px}
  .card-back ul{list-style:none}
  .map-area{width:92px;height:100%;border-radius:2px;background:linear-gradient(135deg,var(--map-road),var(--map-base))}
  .c1{left:580px;top:70px}.c2{left:850px;top:70px}
  .c3{left:580px;top:233px}.c4{left:850px;top:233px}

  /* Envelopes */
  .envelope{width:520px;height:226px;left:580px}
  .env-front{top:410px;padding:22px 26px}
  .env-front .brand-name{font-size:18px}
  .env-front .return{font-size:7px;line-height:1.6;color:var(--muted);margin-top:6px}
  .env-front .watermark{font-size:52px;right:24px;bottom:18px}
  .env-back{top:660px}
  .env-back svg{position:absolute;inset:0}
  .env-back .brand-name{position:absolute;left:0;right:0;top:40px;text-align:center;color:#fff;font-size:15px}
</style>
</head>
<body>

<section class="sheet letterhead">
  <div class="brand-name">Kelvo Car Audio</div>
  <div class="tagline">Car Audio · Security · Tint</div>
  <div class="letter">
    <p>June 12, 2024</p>
    <p class="recipient">Client Name<br>Company Name<br>Street Address<br>City, State ZIP</p>
    <p>Dear Client,</p>
    <p>Thank you for choosing us for your vehicle audio and security needs. Our team installs every system with care and stands behind the work we deliver.</p>
    <p>Please review the enclosed quote and call us with any questions before your appointment date.</p>
    <p>We look forward to working with you.</p>
    <div class="signoff">Sincerely,<strong>Marcus Feltin</strong>President / CEO</div>
  </div>
  <div class="watermark" aria-hidden="true">Kelvo</div>
  <div class="letter-footer">
    <span>4182 W. Linden Ave. Santa Ana, CA 92817</span>
    <span>(714) 555-0142</span>
    <span>marc@kelvocaraudio.example</span>
    <span>www.kelvocaraudio.example</span>
  </div>
</section>

<section class="sheet card card-front c1">
  <div class="brand-name">Kelvo</div>
  <div class="holder"><b>Marcus Feltin</b><span>President / CEO</span></div>
  <div class="contact">4182 W. Linden Ave.<br>Santa Ana, CA 92817<br>(714) 555-0142<br>marc@kelvocaraudio.example<br>www.kelvocaraudio.example</div>
</section>
<section class="sheet card card-back c2">
  <div class="services">
    <h4>Our Services</h4>
    <ul>
      <li>Car Audio Sales and Installation</li>
      <li>Remote Start / Vehicle Security</li>
      <li>GPS Navigation</li>
      <li>Phone &amp; Wireless Integration</li>
      <li>Custom and Pre-Fab Enclosures</li>
      <li>Professional Window Tint</li>
    </ul>
    <h4 class="find">Find Us</h4>
  </div>
  <div class="map-area" role="img" aria-label="Street map showing the shop location"></div>
</section>
<section class="sheet card card-front c3">
  <div class="brand-name">Kelvo</div>
  <div class="holder"><b>Marcus Feltin</b><span>President / CEO</span></div>
  <div class="contact">4182 W. Linden Ave.<br>Santa Ana, CA 92817<br>(714) 555-0142<br>marc@kelvocaraudio.example<br>www.kelvocaraudio.example</div>
</section>
<section class="sheet card card-back c4">
  <div class="services">
    <h4>Our Services</h4>
    <ul>
      <li>Car Audio Sales and Installation</li>
      <li>Remote Start / Vehicle Security</li>
      <li>GPS Navigation</li>
      <li>Phone &amp; Wireless Integration</li>
      <li>Custom and Pre-Fab Enclosures</li>
      <li>Professional Window Tint</li>
    </ul>
    <h4 class="find">Find Us</h4>
  </div>
  <div class="map-area" role="img" aria-label="Street map showing the shop location"></div>
</section>

<section class="sheet envelope env-front">
  <div class="brand-name">Kelvo Car Audio</div>
  <div class="return">4182 W. Linden Ave.<br>Santa Ana, CA 92817</div>
  <div class="watermark" aria-hidden="true">Kelvo</div>
</section>

<section class="sheet envelope env-back">
  <svg width="520" height="226" viewBox="0 0 520 226" aria-hidden="true">
    <polygon points="0,0 520,0 260,92" fill="var(--card-dark)"/>
    <polyline points="0,226 260,120 520,226" fill="none" stroke="#e2e2e2" stroke-width="1"/>
  </svg>
  <div class="brand-name">Kelvo</div>
</section>

</body>
</html>
```